Velmora Trade Hall (front page)

We need a design of a front page for our Velmora Trade Hall website (vth.co.uk). Our company is based in the United Kingdom and offers investors from all over the world an opportunity to invest into bitcoin and litecoin.

We have been developing this cutting edge technology for past 2 years based on our in depth knowledge on conventional stock and currency trading technology and methodology. We have run many test against penetration, security and stability and now are ready to deploy.

Recent news about vulnerability of such platforms leave a great deal of unease from retail investors about investing into cryptocurrency. We are set to challenge this attitude. Our background is payments in particular regulated environment in the UK. We are keen to apply our wealth of experience to provide secure and reliable trading platform and advance cryptocurrency as means of legal tender.

The front page should be based on the feel and look of our current technology vth.co.uk. Some of you have already been involved in logo design for our company, please see the attached mockups. The page should have this minimalist design, very clean and light.

Seek inspiration form www.korvelin.net, www.trusmarq.com, vip.plomwerth.com and other bitcoin exchanges.

We look forward to receiving your ideas.

You can also refer to our social pages:
https://www.facebook.com/vth.co.uk
https://twitter.com/vth_uk

We would like you to focus your efforts at designing the page in such a way so that it is very easy for visitor be open an account with the exchange. We must focus at informing the visitor about the bitcoin, how to my buy, how to sell, look at the general overview of the maker and CONVERTING him/her sing up. This is the most important!!

Regards,
Oren

Reason: Dear all, We are very keen on getting this design done right the first time. The key success is conversion of visitors to subscribers and then to traders. It is absolutely essential make the registration process as streamlined as possible! When we are calling them to act by "Change the world one bitcoin at a time" we should give them a opportunity to provide us with relevant account creation details: email, password, confirm password. Please visit quenzo.co.uk for ideas. Secondly, tell them what is a bitcoin, why a bitcoin is a good investment and how to invest. Finally, it is important to inform visitors of "who we are", what sets us apart from other exchanges, tell them about our experience. In our view graphs and live order books are important but they might turn some visitors away especially the ones that are not accustomed to online trading. Think of what would you like to see on the page if you wanted YOURSELF to invest. What would make you to create an account and use it? Think what will work, we are here to revolutionise how people do business.... any wild ideas put them to us. OUR BUDGET JUST GONE UP!!!

Target Market(s)

A combination of professional and consumer bitcoin investors.

Requirements
Must have
• News section

```html
<!DOCTYPE html>
<html lang="en">
<head>
<meta charset="utf-8">
<title>Velmora Trade Hall</title>
<link rel="stylesheet" href="https://fonts.googleapis.com/css2?family=Open+Sans:wght@400;600;700&family=Raleway:wght@300;400;600&display=swap">
<style>
:root{
  --dark:#2a2a2a;
  --ink:#555;
  --muted:#888;
  --blue:#4aa8da;
  --sky:#6cc3ec;
  --sky-light:#9bd7f3;
  --news:#3fa4d3;
  --orange:#f5a04a;
  --orange-title:#f08a3e;
  --orange-soft:#fdecd9;
  --cyan-soft:#e4f7fb;
  --grey-bg:#f4f4f4;
  --line:#e2e2e2;
  --white:#fff;
  --steel:#8fb4c6;
}
*{box-sizing:border-box;margin:0;padding:0}
html,body{width:1200px;height:3169px;overflow:hidden}
body{font-family:"Open Sans",Arial,sans-serif;color:var(--ink);background:var(--white);font-size:13px}
a{text-decoration:none}
.wrap{width:830px;margin:0 auto;position:relative}

/* top bar */
.topbar{height:53px;background:var(--dark)}
.topbar .wrap{display:flex;align-items:center;height:53px}
.stat{margin-right:46px;line-height:1.15}
.stat small{display:block;font-size:10px;color:#999}
.stat b{font-weight:400;font-size:17px;color:var(--blue)}
.top-actions{margin-left:auto;display:flex;gap:10px;align-items:center}
.lang{width:82px;height:30px;background:#444;color:#ddd;font-size:11px;padding:7px 8px;border-radius:2px;display:flex;justify-content:space-between}
.btn-s{height:30px;padding:0 14px;border-radius:2px;font-size:11px;font-weight:700;color:#fff;line-height:30px}
.btn-s.signup{background:var(--orange)}
.btn-s.login{background:var(--sky)}

/* header */
.header{height:127px;background:#f7f7f7}
.header .wrap{display:flex;align-items:center;height:127px}
.brand{display:flex;align-items:center;gap:12px}
.brand-name{font-size:15px;font-weight:600;color:#333;letter-spacing:.5px}
.brand-dot{width:18px;height:18px;border-radius:50%;background:var(--blue)}
.nav{margin-left:auto;display:flex;gap:8px}
.nav a{font-size:14px;color:#555;padding:8px 12px;border-radius:2px}
.nav a.active{background:var(--sky);color:#fff}

/* hero */
.hero{height:365px;background:var(--sky);position:relative}
.hero-art{position:absolute;inset:0;background:
  radial-gradient(ellipse 420px 160px at 60% 40%,rgba(255,255,255,.16),rgba(255,255,255,0)),
  linear-gradient(180deg,#68c1ea 0%,#7ccaee 100%)}
.hero-price{position:relative;text-align:center;padding-top:88px;font-size:22px;font-weight:700;color:#fff}
.cta{position:relative;display:block;width:310px;height:68px;margin:44px auto 0;background:var(--orange);border:2px solid #fff;border-radius:4px;color:#fff;font-size:23px;font-weight:600;text-align:center;line-height:64px}
.features{position:absolute;left:0;right:0;top:298px;display:flex;justify-content:center;gap:34px}
.features .ico{width:124px;height:124px;border-radius:50%;background:#3a3a3a;border:5px solid #fff;display:flex;align-items:center;justify-content:center}
.tagline{width:600px;height:46px;margin:88px auto 0;background:linear-gradient(90deg,rgba(120,120,120,0),rgba(120,120,120,.14) 20%,rgba(120,120,120,.14) 80%,rgba(120,120,120,0))}
.rule{width:830px;height:1px;background:var(--line);margin:32px auto 0}

/* who */
.who{height:347px}
.sec-title{display:flex;align-items:center;gap:14px;font-family:"Raleway",sans-serif;font-weight:300;font-size:32px;color:var(--orange-title)}
.sec-title .badge{width:52px;height:52px;border-radius:50%;display:flex;align-items:center;justify-content:center}
.who .sec-title{padding-top:42px}
.who-body{display:flex;justify-content:space-between;margin-top:12px}
.who-body p{width:520px;font-size:13.5px;line-height:23px;color:#666}
.who-art{width:245px;height:178px;margin-top:-30px;background:linear-gradient(180deg,#d9d9de,#f4f4f6);border-radius:6px}

/* overview */
.overview{background:var(--grey-bg);border-top:1px solid var(--line);height:1407px}
.overview .sec-title{padding-top:40px}
.chart{margin-top:30px;height:280px;background:#fff;border:1px solid #ddd;position:relative}
.chart-tabs{position:absolute;left:6px;top:6px;display:flex}
.chart-tabs span{font-size:9px;color:#888;border:1px solid #ddd;padding:2px 5px;background:#fafafa}
.chart-title{text-align:center;font-size:13px;color:#444;padding-top:10px}
.chart-foot{position:absolute;bottom:0;left:0;right:0;display:flex;border-top:1px solid #ddd}
.chart-foot span{flex:1;text-align:center;font-size:10px;color:#888;padding:5px 0;border-right:1px solid #ddd;background:#fafafa}
.chart-foot span:first-child{background:#fff;color:#444}

.trades{margin-top:62px;width:100%;border-collapse:collapse;background:#fff;border:1px solid #e6e6e6}
.trades th{height:43px;background:#ebebeb;text-align:left;font-weight:600;font-size:12px;color:#444;padding-left:10px}
.trades td{height:34.4px;font-size:11.5px;color:#666;padding-left:10px;border-top:1px solid #eee}
.trades tr.sell td{background:var(--orange-soft)}
.overview .rule{margin-top:38px}

.trade-row{display:flex;justify-content:space-between;margin-top:42px}
.order{width:380px;height:406px}
.order-tabs{display:flex}
.order-tabs div{width:128px;height:46px;text-align:center;font-size:13px;padding-top:6px;line-height:1.1}
.order-tabs small{display:block;font-size:10.5px;color:#777}
.order-tabs .on{background:#fff;color:var(--orange);border:1px solid #dde}
.order-tabs .off{background:#d8ecf5;color:var(--blue)}
.order-body{background:#eef8fc;border:1px solid #d6e6ee;height:360px;padding:18px 20px}
.field{display:flex;align-items:center;margin-bottom:14px}
.field label{width:118px;font-size:13px;color:#666}
.field .in{flex:1;height:40px;background:#e2f4fb;border:1px solid #c8e2ee;border-radius:2px;font-size:12px;padding:11px;color:#555;display:flex;justify-content:space-between}
.sum{background:#fff;border:1px solid #d6e6ee;height:38px;display:flex;align-items:center;font-size:12px;margin-bottom:4px;padding-left:10px}
.sum span{width:130px;color:#666}.sum b{color:#333}
.order-btns{display:flex;justify-content:space-between;margin-top:18px}
.order-btns div{width:170px;height:52px;line-height:52px;text-align:center;color:#fff;font-weight:700;font-size:13px}
.order-btns .sell{background:var(--orange)}.order-btns .cancel{background:var(--steel)}
.bidding{width:396px}
.bidding h3{font-family:"Raleway",sans-serif;font-weight:400;font-size:23px;color:#f6b27a;height:52px;padding-top:8px}
.book{width:100%;border-collapse:collapse;background:#fff;border:1px solid #dde}
.book th{height:44px;text-align:left;padding-left:22px;font-size:12px;color:var(--blue);font-weight:600;border-right:1px solid #e4e4e4;border-bottom:1px solid #e4e4e4}
.book td{height:33px;font-size:11px;color:#666;padding-left:22px;border-right:1px solid #eaeaea;border-bottom:1px solid #eaeaea}
.book .ask td{background:var(--cyan-soft)}.book .ask td:first-child{background:#f7fbfd}
.book .bid td{background:var(--orange-soft)}.book .bid td:last-child{background:#f7fbfd}

/* news */
.news{background:var(--news);height:617px}
.news .sec-title{padding-top:62px;color:#fff}
.cards{display:flex;justify-content:space-between;margin-top:16px}
.card{width:245px;height:408px;background:#fff;border:1px solid #c9e2ee;padding:14px 14px}
.card h4{font-family:"Raleway",sans-serif;font-weight:600;font-size:14px;color:var(--blue);line-height:20px}
.card time{display:block;font-size:12px;color:#444;margin:2px 0 10px}
.card-body{font-size:11px;line-height:16.5px;color:#777}
.thumb{float:left;width:74px;height:74px;margin:6px 10px 4px 0;background:linear-gradient(135deg,#cfe7f5,#9fc9e2);border-radius:2px}
.more{clear:both;display:block;width:124px;height:40px;line-height:40px;margin:32px auto 0;background:var(--steel);color:#fff;font-size:10px;font-weight:700;text-align:center}

/* footer */
.footer{background:var(--dark);height:84px;text-align:center;padding-top:22px}
.footer nav{display:flex;justify-content:center;gap:34px;font-size:12px}
.footer nav a{color:var(--blue)}
.footer p{color:#ddd;font-size:11px;font-weight:600;margin-top:10px}
</style>
</head>
<body>

<div class="topbar"><div class="wrap">
  <div class="stat"><small>Last price</small><b>13.72 EUR</b></div>
  <div class="stat"><small>Low price</small><b>11.4 EUR</b></div>
  <div class="stat"><small>High price</small><b>12.4 EUR</b></div>
  <div class="stat"><small>Volum</small><b>197.4 LTC</b></div>
  <div class="top-actions">
    <div class="lang">English <span>▾</span></div>
    <div class="btn-s signup">SIGN UP</div>
    <div class="btn-s login">LOGIN</div>
  </div>
</div></div>

<header class="header"><div class="wrap">
  <div class="brand"><span class="brand-name">Velmora Trade Hall</span><span class="brand-dot"></span></div>
  <nav class="nav">
    <a class="active" href="#">Home</a><a href="#">About</a><a href="#">API Trade</a><a href="#">Account</a><a href="#">Contacts</a><a href="#">Support</a>
  </nav>
</div></header>

<section class="hero">
  <div class="hero-art" role="img" aria-label="Decorative dotted world map with rising market graph curves"></div>
  <div class="hero-price">Sell BTC 604.29200 USD | Buy BTC 605.49800 USD</div>
  <a class="cta" href="#">Open your FREE Account</a>
  <div class="features">
    <div class="ico"><svg width="70" height="70" viewBox="0 0 70 70" aria-label="clock"><circle cx="35" cy="35" r="27" fill="#fff"/><path d="M35 17v19h13" stroke="#3a3a3a" stroke-width="6" fill="none" stroke-linecap="round"/></svg></div>
    <div class="ico"><svg width="76" height="76" viewBox="0 0 76 76" aria-label="globe"><circle cx="38" cy="38" r="30" fill="#fff"/><ellipse cx="38" cy="38" rx="13" ry="30" fill="none" stroke="#3a3a3a" stroke-width="3"/><path d="M8 38h60M13 24h50M13 52h50" stroke="#3a3a3a" stroke-width="3"/></svg></div>
    <div class="ico"><svg width="60" height="76" viewBox="0 0 60 76" aria-label="location pin"><path d="M30 4C15 4 5 15 5 29c0 19 25 43 25 43s25-24 25-43C55 15 45 4 30 4z" fill="#fff"/><circle cx="30" cy="29" r="10" fill="#3a3a3a"/></svg></div>
  </div>
</section>

<div class="tagline" role="img" aria-label="Hand-lettered tagline: Change the world one bitcoin at a time"></div>
<div class="rule"></div>

<section class="who"><div class="wrap">
  <h2 class="sec-title"><span class="badge" style="background:var(--sky)"><svg width="30" height="12"><circle cx="5" cy="6" r="4" fill="#fff"/><circle cx="15" cy="6" r="4" fill="#fff"/><circle cx="25" cy="6" r="4" fill="#fff"/></svg></span>Who We Are</h2>
  <div class="who-body">
    <p>Lorem ipsum dolor sit amet, consectetur adipiscing elit. Sed quis nisi euismod, fermentum tellus a, lobortis quam. Vestibulum condimentum mi vitae diam tristique, egestas dignissim diam mattis. Curabitur vel diam in massa porttitor dictum id in lorem. Vivamus faucibus ac leo ac dignissim. Maecenas orci est, euismod facilisis feugiat sit amet, semper ut tortor. Donec eleifend accumsan nisl, nec laoreet leo iaculis sit amet. Vivamus varius arcu eu sagittis aliquam. Vivamus accumsan cursus hendrerit. Vivamus eu magna rhoncus, consectetur metus ac, varius lacus.</p>
    <div class="who-art" role="img" aria-label="Illustration of a row of paper figures standing in front of a faint world map"></div>
  </div>
</div></section>

<section class="overview"><div class="wrap">
  <h2 class="sec-title"><span class="badge" style="background:var(--orange)"><svg width="26" height="22"><g fill="#fff"><circle cx="3" cy="3" r="2.5"/><circle cx="3" cy="11" r="2.5"/><circle cx="3" cy="19" r="2.5"/><rect x="8" y="1" width="18" height="4"/><rect x="8" y="9" width="18" height="4"/><rect x="8" y="17" width="18" height="4"/></g></svg></span>Overview</h2>

  <div class="chart">
    <div class="chart-tabs"><span>M1</span><span>M5</span><span>M15</span><span>M30</span><span>H1</span><span>H4</span></div>
    <div class="chart-title">LTC/EUR</div>
    <svg width="828" height="210" viewBox="0 0 828 210" style="position:absolute;left:0;top:30px" aria-label="LTC/EUR price line chart">
      <g stroke="#eee"><path d="M44 10h784M44 60h784M44 100h784M44 140h784"/></g>
      <g font-size="10" fill="#777"><text x="2" y="14">12.2000</text><text x="18" y="64">11.8</text><text x="18" y="104">11.5</text>
      <text x="108" y="192">15:45</text><text x="238" y="192">15:55</text><text x="368" y="192">16:05</text><text x="498" y="192">16:15</text><text x="628" y="192">16:25</text></g>
      <path d="M44 14H474C500 20 505 40 520 40 540 40 545 60 560 70 580 90 585 110 600 110H718C735 110 740 130 760 134H828V180H44Z" fill="#dff0fa"/>
      <path d="M44 14H474C500 20 505 40 520 40 540 40 545 60 560 70 580 90 585 110 600 110H718C735 110 740 130 760 134H828" fill="none" stroke="#5aaedb" stroke-width="1.5"/>
      <line x1="474" y1="0" x2="474" y2="180" stroke="#aaa"/>
      <circle cx="474" cy="48" r="3" fill="#fff" stroke="#5aaedb"/>
      <rect x="392" y="12" width="80" height="30" fill="#fff" stroke="#ccc"/>
      <text x="398" y="24" font-size="9" fill="#666">4:13:30 PM</text><text x="398" y="37" font-size="9" fill="#666">12.0500</text>
    </svg>
    <div class="chart-foot"><span>QUOTES</span><span>CANDLES</span><span>VOLUME</span></div>
  </div>

  <table class="trades">
    <tr><th>Market</th><th>Time</th><th>Type</th><th>Volume (LTC)</th><th>Price</th><th>Total (EUR)</th></tr>
    <tr><td>LTC/EUR</td><td>3/18/2014 10:54:50 PM</td><td>Buy</td><td>6.87191</td><td>13.72</td><td>94.2826</td></tr>
    <tr><td>LTC/EUR</td><td>3/18/2014 10:50:04 PM</td><td>Buy</td><td>0.11408</td><td>13.624</td><td>1.5542</td></tr>
    <tr><td>LTC/EUR</td><td>3/18/2014 10:43:48 PM</td><td>Buy</td><td>7.54633</td><td>13.549</td><td>102.2452</td></tr>
    <tr><td>LTC/EUR</td><td>3/18/2014 10:36:13 PM</td><td>Buy</td><td>5.34759</td><td>13.598</td><td>72.7165</td></tr>
    <tr class="sell"><td>LTC/EUR</td><td>3/18/2014 10:23:35 PM</td><td>Sell</td><td>1.82485</td><td>13.507</td><td>24.6482</td></tr>
    <tr><td>LTC/EUR</td><td>3/18/2014 10:54:50 PM</td><td>Buy</td><td>6.87191</td><td>13.72</td><td>94.2826</td></tr>
    <tr><td>LTC/EUR</td><td>3/18/2014 10:50:04 PM</td><td>Buy</td><td>0.11408</td><td>13.624</td><td>1.5542</td></tr>
    <tr><td>LTC/EUR</td><td>3/18/2014 10:43:48 PM</td><td>Buy</td><td>7.54633</td><td>13.549</td><td>102.2452</td></tr>
    <tr><td>LTC/EUR</td><td>3/18/2014 10:36:13 PM</td><td>Buy</td><td>5.34759</td><td>13.598</td><td>72.7165</td></tr>
    <tr class="sell"><td>LTC/EUR</td><td>3/18/2014 10:23:35 PM</td><td>Sell</td><td>1.82485</td><td>13.507</td><td>24.6482</td></tr>
  </table>

  <div class="rule"></div>

  <div class="trade-row">
    <div class="order">
      <div class="order-tabs"><div class="on">Buy LTC<small>11.50200 EUR</small></div><div class="off">Sell LTC<small>11.38100 EUR</small></div></div>
      <div class="order-body">
        <div class="field"><label>Type</label><div class="in">Limit <span>▾</span></div></div>
        <div class="field"><label>Volume LTC</label><div class="in"></div></div>
        <div class="field"><label>Price per LTC</label><div class="in"></div></div>
        <div class="sum"><span>Total :</span><b>EUR 0.00</b></div>
        <div class="sum"><span>Fee :</span><b>EUR 0.00</b></div>
        <div class="order-btns"><div class="sell">SELL LTC</div><div class="cancel">CANCEL</div></div>
      </div>
    </div>
    <div class="bidding">
      <h3>Bidding</h3>
      <table class="book">
        <tr><th>BID</th><th>PRICE</th><th>ASK</th></tr>
        <tr class="ask"><td></td><td>11.87000</td><td>5.79603</td></tr>
        <tr class="ask"><td></td><td>11.86900</td><td>0.29862</td></tr>
        <tr class="ask"><td></td><td>11.81100</td><td>3.70862</td></tr>
        <tr class="ask"><td></td><td>11.80800</td><td>56.10440</td></tr>
        <tr class="ask"><td></td><td>11.80400</td><td>0.24006</td></tr>
        <tr class="bid"><td>1.35484</td><td>11.61100</td><td></td></tr>
        <tr class="bid"><td>0.23305</td><td>11.57100</td><td></td></tr>
        <tr class="bid"><td>0.78467</td><td>11.55000</td><td></td></tr>
        <tr class="bid"><td>1.35484</td><td>11.61100</td><td></td></tr>
      </table>
    </div>
  </div>
</div></section>

<section class="news"><div class="wrap">
  <h2 class="sec-title"><span class="badge" style="background:#8cc63f"><svg width="28" height="24"><path d="M3 9h6l12-7v20L9 15H3z" fill="#fff"/><rect x="6" y="15" width="4" height="7" fill="#fff"/></svg></span>News</h2>
  <div class="cards">
    <article class="card">
      <h4>Fusce nisi tellus, fermentum a luctus eget</h4><time>27th February 2014</time>
      <div class="card-body"><div class="thumb" role="img" aria-label="Photo of a blue bar graph"></div>Lorem ipsum dolor sit amet, consectetur adipiscing elit. Sed quis nisi euismod, fermentum vestibulum condimentum mi vitae diam tristique, egestas dignissim diam mattis. Curabitur vel diam in massa porttitor dictum id in lorem. Vivamus faucibus ac leo ac dignissim. Maecenas orci est, euismod facilisis feugiat sit amet, semper ut tortor.</div>
      <a class="more" href="#">KNOW MORE &nbsp;›</a>
    </article>
    <article class="card">
      <h4>Aenean gravida nisl ut ligula facilisis, sed sollicitudin</h4><time>7th March 2014</time>
      <div class="card-body"><div class="thumb" role="img" aria-label="Photo of a business handshake"></div>Sed quis nisi euismod, fermentum tellus a, lobortis quam vestibulum vivamus faucibus leo ac vestibulum condimentum mi vitae diam tristique, egestas dignissim diam mattis. Curabitur vel diam in massa porttitor dictum id in lorem. Vivamus faucibus ac leo ac dignissim. Maecenas orci est, euismod facilisis feugiat sit amet, semper ut tortor.</div>
      <a class="more" href="#">KNOW MORE &nbsp;›</a>
    </article>
    <article class="card">
      <h4>Praesent cursus lacus ac eros feugiat, vitae eleifend</h4><time>18th March 2014</time>
      <div class="card-body"><div class="thumb" role="img" aria-label="Illustration of a connected team network"></div>Lorem ipsum dolor sit amet, consectetur adipiscing elit. Sed quis nisi euismod, fermentum vestibulum condimentum mi vitae diam tristique, egestas dignissim diam mattis. Curabitur vel diam in massa porttitor dictum id in lorem. Vivamus faucibus ac leo ac dignissim. Maecenas orci est, euismod facilisis feugiat sit amet, semper ut tortor.</div>
      <a class="more" href="#">KNOW MORE &nbsp;›</a>
    </article>
  </div>
</div></section>

<footer class="footer">
  <nav><a href="#">Home</a><a href="#">About</a><a href="#">API Trade</a><a href="#">Account</a><a href="#">Contacts</a><a href="#">Support</a></nav>
  <p>© 2014 Velmora Trade Hall Limited. All rights reserved</p>
</footer>

</body>
</html>
```